Simple Easy - Taekwondo brochure

I have the content and an idea of the layout I want. I need it to look nice and sharp.

It's a sided 8.5x11 colored brochure

please feel free to move things around and use the images provided

my website is www.brightpathdojo.example if you need an understanding of what the business is about.

all text content is on the website. please be creative!

Target Market(s)

Mothers...must by family friendly because it's for mothers to bring their kids.

Industry/Entity Type

Martial Art

Font styles to use
Other font styles liked:
• Lato

```html
<!DOCTYPE html>
<html lang="en">
<head>
<meta charset="utf-8">
<title>Bright Path Dojo – Trifold Brochure</title>
<link href="https://fonts.googleapis.com/css2?family=Lato:wght@400;700;900&display=swap" rel="stylesheet">
<style>
:root{
  --red:#c81e2a;
  --red-dark:#8e0f18;
  --blue:#1b6fc0;
  --black:#111;
  --ink:#2b2b2b;
  --paper:#ffffff;
  --stage:#d7d7d7;
  --map:#d9dbdd;
}
*{box-sizing:border-box;margin:0;padding:0}
html,body{width:1200px;height:1200px;overflow:hidden;background:var(--stage);font-family:'Lato',sans-serif;color:var(--ink)}
.brochure{position:absolute;left:40px;top:167px;width:1120px;height:866px;display:flex;background:var(--paper);box-shadow:0 10px 30px rgba(0,0,0,.18)}
.panel{position:relative;width:373.33px;height:100%;overflow:hidden;border-right:1px solid #eee}
.panel:last-child{border-right:none}

/* Bio panel */
.corner-accent{position:absolute;left:0;top:0;width:130px;height:150px;clip-path:polygon(0 0,100% 0,0 100%);background:linear-gradient(135deg,var(--black),var(--red) 55%,var(--blue))}
.bio-photo{position:absolute;left:110px;top:18px;width:245px;height:170px;background:linear-gradient(160deg,#f4f5f7,#e6e8eb);border-radius:4px}
.bio{position:absolute;left:30px;right:26px;top:200px}
.bio h2{color:var(--blue);font-size:24px;font-weight:900;margin-bottom:6px}
.bio p{font-size:10.6px;line-height:1.42;margin-bottom:6px}
.awards h3{font-size:14px;color:var(--red);font-weight:900;margin-top:8px}
.awards h3 .star{color:var(--black);letter-spacing:2px}
.awards .sub{font-size:12px;margin-bottom:6px}
.awards ul{list-style:none}
.awards li{font-size:11.5px;line-height:1.35;padding-left:14px;position:relative;margin-bottom:4px}
.awards li::before{content:"";position:absolute;left:0;top:6px;width:6px;height:6px;border-radius:50%;background:var(--blue)}

/* Offer panel */
.offer{position:absolute;left:30px;right:30px;top:30px;text-align:center}
.offer h2{color:var(--red);font-size:20px;font-weight:900}
.offer .author{font-size:11px;font-weight:700;margin:3px 0 8px}
.quote{position:relative;font-size:10.4px;line-height:1.45;text-align:left;padding-left:18px}
.quote .mark{position:absolute;left:0;top:-4px;color:var(--red);font-size:26px;font-weight:900;line-height:1}
.quote .mark.end{position:static;display:block;text-align:center;font-size:22px;margin-top:2px}
.deal{margin-top:20px;font-size:17px;line-height:1.2}
.deal .pct{color:var(--red);font-weight:900}
.deal .shirt{display:block;color:var(--blue);font-size:31px;font-weight:900;letter-spacing:.5px}
.map{width:180px;height:180px;margin:18px auto 0;border-radius:50%;background:radial-gradient(circle at 40% 40%,#ecebe6,var(--map))}
.contact{margin-top:26px;text-align:center}
.contact h3{color:var(--red);font-size:20px;font-weight:900}
.contact .line{display:flex;align-items:center;justify-content:center;gap:6px;font-size:14px;margin-top:4px}
.contact .line svg{flex:none}

/* Cover panel */
.brand{position:absolute;top:46px;left:0;right:0;text-align:center}
.brand .dot{display:inline-block;width:56px;height:56px;border-radius:50%;background:var(--red);margin-bottom:10px}
.brand .name{font-size:23px;font-weight:900;color:var(--red);letter-spacing:.5px}
.brand .tag{font-size:11px;margin-top:3px}
.cover-photo{position:absolute;left:36px;top:170px;width:300px;height:300px;background:linear-gradient(180deg,#eef0f2,#d9dde1);border-radius:4px}
.cover-accent{position:absolute;left:0;right:0;bottom:0;height:360px;clip-path:polygon(100% 0,100% 45%,30% 100%,0 100%,0 75%);background:linear-gradient(160deg,var(--blue) 0%,var(--red) 35%,var(--red-dark) 75%,var(--black))}
.site{position:absolute;right:22px;bottom:34px;font-size:13px;font-weight:700;color:var(--black)}
</style>
</head>
<body>
<main class="brochure">

  <section class="panel panel-bio">
    <div class="corner-accent" role="img" aria-label="Decorative corner accent in red, blue and black"></div>
    <div class="bio-photo" role="img" aria-label="Faint photo of children practising taekwondo kicks"></div>
    <article class="bio">
      <h2>Master Ren</h2>
      <p>Renato Kwan (Master Ren) is the owner and head instructor at Bright Path Dojo. Master Ren is a Central Academy certified 3rd degree Black Belt. Central Academy is the overseeing authority of all Black Belts in the world, working with the Global Taekwondo Union (GTU); it also oversees taekwondo in international competition. In 1992, at the age of 8, Master Ren began training under Grand Master Alvarez, who achieved the level of 8th Dan in taekwondo under the International Martial Arts Council (IMAC). The IMAC is another highly respected global authority for taekwondo.</p>
      <p>When Master Ren entered Middle School and then High School, his years of taekwondo training became invaluable as he participated in wrestling, track, and hockey.</p>
      <p>Master Ren continued his taekwondo training post-high school, and in 2007 began training under Grand Master Dorin, who has achieved the level of 6th Dan in Central Academy taekwondo. Grand Master Dorin was also a distinguished member of the national team that competed around the world.</p>
      <p>While attending Riverside University, Master Ren joined the university taekwondo team. Upon graduating in 2008, he was invited by the team to become its Assistant Coach. Because of his exceptional skill and his ability to positively influence and motivate the team, the University selected him to lead as Head Coach from 2010–2013.</p>
      <p>In 2013, Master Ren began training under Grand Master Velan, a 9th Dan in Taekwondo. Master Ren currently trains under Grand Master Velan.</p>
      <div class="awards">
        <h3><span class="star">★★★</span> AWARDS | ACHIEVEMENTS <span class="star">★★★</span></h3>
        <p class="sub">(under Master Ren's leadership)</p>
        <ul>
          <li>4 National Taekwondo League State Medalists, GTU sanctioned</li>
          <li>10 State Championships, GTU sanctioned</li>
          <li>12 Coastal Collegiate Martial Arts Conference (CCMAC) Team Medals, GTU sanctioned</li>
          <li>1 CCMAC Top Division Team Title, GTU sanctioned</li>
        </ul>
      </div>
    </article>
  </section>

  <section class="panel panel-offer">
    <div class="offer">
      <h2>Testimonial</h2>
      <p class="author">Sara L.</p>
      <blockquote class="quote">
        <span class="mark">&ldquo;</span>
        I started taking classes with Master Ren a little over 3 years ago. As the newest member of the class, I was shy and unsure of myself. However, I quickly overcame those feelings because Master Ren is a natural teacher. Paired with his passion for the sport, his gift for teaching makes him one of the best coaches I have encountered. I have seen him work with both children and adults, and his manner is unfailingly supportive and encouraging. As a teacher myself, I see how he tailors his teaching style to each student, and I hope to follow his example in my classroom. I am thankful that my first experience with taekwondo has been through Master Ren's class.
        <span class="mark end">&rdquo;</span>
      </blockquote>
      <p class="deal">Special Offer: <span class="pct">50% off</span> trial lessons<br>and get a <span class="shirt">FREE T-SHIRT!</span></p>
      <div class="map" role="img" aria-label="Street map showing the dojo location"></div>
      <div class="contact">
        <h3>CALL US TODAY!</h3>
        <p class="line">
          <svg width="12" height="12" viewBox="0 0 24 24" aria-hidden="true"><path fill="var(--blue)" d="M6.6 10.8a15 15 0 0 0 6.6 6.6l2.2-2.2a1 1 0 0 1 1-.25 11.4 11.4 0 0 0 3.6.57 1 1 0 0 1 1 1V20a1 1 0 0 1-1 1A17 17 0 0 1 3 4a1 1 0 0 1 1-1h3.5a1 1 0 0 1 1 1c0 1.25.2 2.45.57 3.57a1 1 0 0 1-.25 1z"/></svg>
          555-014-2290
        </p>
        <p class="line">
          <svg width="12" height="14" viewBox="0 0 24 28" aria-hidden="true"><path fill="var(--blue)" d="M12 0a10 10 0 0 0-10 10c0 7.5 10 18 10 18s10-10.5 10-18A10 10 0 0 0 12 0zm0 14a4 4 0 1 1 0-8 4 4 0 0 1 0 8z"/></svg>
          2280 Orchard Lane
        </p>
        <p class="line">Maple Ridge, PA 19000</p>
      </div>
    </div>
  </section>

  <section class="panel panel-cover">
    <header class="brand">
      <span class="dot" aria-hidden="true"></span>
      <h1 class="name">BRIGHT PATH DOJO</h1>
      <p class="tag">Focus Your Child's Potential</p>
    </header>
    <div class="cover-photo" role="img" aria-label="Instructor in white uniform with black collar, arms crossed, with faint action photos behind"></div>
    <div class="cover-accent" role="img" aria-label="Decorative diagonal colour field in red, blue and black"></div>
    <p class="site">www.brightpathdojo.example</p>
  </section>

</main>
</body>
</html>
```